Medical Breast Thermography Brochure Needed

Looking for a brochure that matches the theme and overall look/feel of our website brookhavenhc.com.

http://brookhavenhc.com/ourservices/breast-thermography/

I have previously used PixelMarket for logo, business card, and brochure and have been very happy, as soon as designs start being submitted I will switch to guaranteed payment.

I'm looking for a professional, clean, simple, minimalist, bold design.
Colors would ideally be greens and blues, or pink, cool tones, muted colors, or graytones.

See attached word document for content for brochure.

I would like to have the TH1-TH5 images in the Corvane thermo brochure 11.pdf document in the brochure.

Also would like one fold to compare mammogram with breast thermography like in BKHC_thermography_vs_mammography.jpg

I have attached a copy of our prior overall practice brochure to see what type of design I would like.

Feel free to use any stock photos.

```html
<!DOCTYPE html>
<html lang="en">
<head>
<meta charset="utf-8">
<title>Breast Thermography Brochure</title>
<link href="https://fonts.googleapis.com/css2?family=Roboto+Condensed:wght@300;400;700&family=Raleway:wght@400;700;800&display=swap" rel="stylesheet">
<style>
:root{
  --pink:#e2737f;
  --pink-soft:#eea4ad;
  --pink-wash:rgba(226,115,127,.82);
  --blue:#2a87ad;
  --navy:#1f5177;
  --ink:#3c3c3e;
  --grey:#d8d8da;
  --grey-light:#efeff0;
  --page:#e6e4e1;
  --white:#ffffff;
  --thermal-warm:#e8823a;
  --thermal-cool:#4a7fc0;
}
*{box-sizing:border-box;margin:0;padding:0}
html,body{width:875px;height:1200px;overflow:hidden;background:var(--page)}
body{font-family:"Roboto Condensed",Arial,sans-serif;color:var(--ink);font-size:6.7px;line-height:1.28;position:relative}
.sheet{position:absolute;left:37px;width:800px;height:545px;display:flex;background:var(--white);box-shadow:0 2px 6px rgba(0,0,0,.18)}
.sheet--outside{top:28px}
.sheet--inside{top:612px}
.panel{position:relative;width:266.67px;height:100%;overflow:hidden;padding:12px 14px}
p{margin-bottom:4px}
.q{color:var(--blue);font-weight:700;font-size:7px;margin-top:5px;margin-bottom:2px}
.ticks{list-style:none}
.ticks li{position:relative;padding-left:11px;margin-bottom:3px}
.ticks li::before{content:"✓";position:absolute;left:0;top:0;width:7px;height:7px;background:var(--pink);color:#fff;font-size:6px;line-height:7px;text-align:center;font-weight:700}

/* facts panel */
.facts-panel{background:linear-gradient(90deg,#fff 0,#fff 85%,#e9e9ea 100%);padding-right:22px}
.facts-title{color:var(--blue);font-weight:700;font-size:7px;margin:6px 0 4px}
.fact{display:flex;align-items:center;gap:6px;padding:3px 0 3px 12px;margin-left:-14px;margin-right:-22px;padding-right:22px;font-size:6.7px}
.fact:nth-child(even){background:var(--grey)}
.fact:nth-child(odd){background:#e8e8ea}
.fact-num{flex:0 0 12px;height:12px;border-radius:50%;background:var(--pink);color:#fff;font-size:5.5px;font-weight:700;display:flex;align-items:center;justify-content:center}

/* pricing panel */
.pricing-panel{background:linear-gradient(90deg,#e4e4e6,#f4f4f5 30%,#f7f7f8)}
.cost-box{background:var(--pink-wash);margin:60px 4px 0;padding:6px 8px 8px;color:#fff}
.cost-box h2{background:var(--navy);color:#fff;font-size:14px;font-weight:700;width:64px;text-align:center;margin:-14px auto 6px;padding:3px 0}
.cost-box p{font-size:5.6px;text-align:center}
.fee-table{border-collapse:collapse;margin:5px 4px 0;width:calc(100% - 8px);font-size:5.6px;background:#f2f2f3}
.fee-table th{background:var(--navy);color:#fff;font-weight:700;padding:3px;font-size:5.6px}
.fee-table td{padding:2.5px 3px;border-bottom:1px solid #fff;vertical-align:top}
.fee-table td:first-child{font-weight:700;width:38px}
.fee-table td:last-child{text-align:center;width:36px;font-weight:700}
.fee-table tr:nth-child(even) td{background:#e3e3e5}
.quality-banner{margin:8px 24px 0;background:var(--navy);color:#fff;font-weight:700;text-align:center;font-size:8.3px;line-height:1.15;padding:3px 4px;border:2px solid #fff;outline:1px solid var(--navy);position:relative;z-index:1}
.call-box{margin:-8px 4px 0;background:var(--pink-wash);color:#fff;text-align:center;padding:16px 8px 8px;font-size:6.3px}
.call-box h3{color:var(--navy);font-weight:400;font-size:10px;margin-bottom:2px}
.call-box .tag{margin-top:5px;font-size:6.4px}
.thermal-row{display:flex;justify-content:space-between;margin:10px 4px 0}
.thermal-dot{width:62px;height:62px;border-radius:50%;border:3px solid var(--pink-soft);background:linear-gradient(135deg,var(--thermal-warm),var(--pink))}

/* cover */
.cover-panel{background:#fff;padding:0}
.brand{position:absolute;top:26px;left:40px;display:flex;align-items:center;gap:8px;z-index:2}
.brand-dot{width:14px;height:14px;border-radius:50%;background:var(--blue)}
.brand-name{font-family:"Raleway",sans-serif;font-weight:700;color:var(--navy);font-size:15px;line-height:1}
.cover-photo{position:absolute;top:64px;left:0;width:100%;height:330px;background:linear-gradient(100deg,#f4f4f4 0,#cfcfcf 45%,#9a9a9a 100%)}
.cover-swoosh{position:absolute;left:0;width:100%}
.cover-title{position:absolute;top:350px;left:0;width:100%;text-align:center;font-family:"Raleway",sans-serif}
.cover-title .big{display:block;font-size:52px;font-weight:800;color:var(--pink);letter-spacing:1px;line-height:1}
.cover-title .sub{display:block;font-size:24px;font-weight:400;color:var(--navy);line-height:1}
.tagline{position:absolute;bottom:18px;left:0;width:100%;display:flex;justify-content:space-around;font-size:14px;text-align:center;line-height:1.05;color:var(--navy)}
.tagline b{font-weight:700}
.tagline span{font-weight:300}

/* inside left */
.intro-panel{background:linear-gradient(90deg,#bdbdbf,#d9d9db 60%,#c9c9cb)}
.intro-card{position:absolute;top:14px;left:14px;right:14px;bottom:8px;background:var(--pink-wash);padding:0 10px 8px;color:#fff}
.intro-card h2{background:var(--navy);color:#fff;font-size:10px;font-weight:400;line-height:1.2;text-align:center;padding:6px;margin:0 -4px 8px;border:2px solid #fff;outline:1px solid var(--navy)}
.intro-card .lead b{font-weight:700}
.intro-card h3{color:var(--navy);font-size:10px;font-weight:400;margin:5px 0 3px}
.intro-card h3 b{font-weight:700}
.intro-card .ticks li::before{background:#fff;color:var(--pink)}
.intro-card .callout{color:var(--navy);font-weight:700}
.stat-block{display:flex;gap:6px;margin-top:4px}
.stat-badge{flex:0 0 112px;background:#fff;padding:4px;text-align:center}
.stat-figure{height:20px;margin:0 auto 3px;width:100px;background:#d6d6d8}
.stat-badge .big{color:var(--pink);font-size:16px;font-weight:700;line-height:1}
.stat-badge .small{color:#222;font-size:6.6px;font-weight:700}

/* inside middle */
.info-panel{background:#fff}
.band{position:relative;background:var(--blue);color:#fff;font-size:9.3px;line-height:1.15;padding:4px 10px;margin:0 -14px 6px;clip-path:polygon(0 0,90% 0,100% 100%,0 100%)}
.band b{font-weight:700}
.sub-head{color:var(--blue);font-size:9.2px;margin:6px 0 3px}
.sub-head b{font-weight:700}
.benefits{display:grid;grid-template-columns:1.7fr 1fr .6fr;gap:2px 4px}
.who li{margin-bottom:2px}
.who .note{list-style:none;padding-left:18px;position:relative;margin-top:1px}
.who .note::before{content:"";position:absolute;left:11px;top:2px;width:3px;height:3px;border:1px solid var(--blue);border-radius:50%;background:none}

/* inside right */
.compare-panel{background:linear-gradient(90deg,#f2f2f3,#fff 20%)}
.compare-panel .band{background:var(--navy)}
.faq-q{color:var(--blue);font-weight:700;font-size:7px;margin:4px 0 2px}
.size-chart{margin:6px 0 2px}
.chart-labels{display:flex;justify-content:space-between;font-size:4.6px;color:#666;text-align:center;line-height:1.1}
.risk-labels{display:flex;justify-content:space-between;margin-top:4px}
.risk-labels span{background:var(--blue);color:#fff;font-size:4.6px;padding:1px 3px}
.th-row{display:flex;gap:3px;margin-top:4px}
.th-item{flex:1}
.th-img{height:40px;background:linear-gradient(180deg,var(--thermal-warm),#c9733f)}
.th-item:first-child .th-img{background:linear-gradient(180deg,var(--thermal-cool),#3a9a8a)}
.th-name{color:var(--navy);font-weight:700;font-size:8.4px;margin-top:2px;line-height:1}
.th-item:not(:first-child) .th-name{color:var(--pink)}
.th-note{font-size:3.9px;line-height:1.2;color:#555}
</style>
</head>
<body>

<section class="sheet sheet--outside">

  <div class="panel facts-panel">
    <div class="facts-title">7 additional facts about thermography vs. mammograms</div>
    <div class="fact-list">
      <div class="fact"><span class="fact-num">01</span><span>Breast thermography has been FDA approved as an adjunct diagnostic tool to mammograms since 1982.</span></div>
      <div class="fact"><span class="fact-num">02</span><span>There have been 800 peer-reviewed breast thermography studies in which over a quarter million women have participated in large-scale studies over 12 years. These studies show thermography to be 90% accurate.</span></div>
      <div class="fact"><span class="fact-num">03</span><span>Mammograms in pre-menopausal women can be up to 89% inaccurate, leading to unnecessary procedures, as well as emotional and physical trauma.</span></div>
      <div class="fact"><span class="fact-num">04</span><span>Many false negatives occur with mammograms since tumors are frequently located in the upper outer aspects of the breasts where the scans do not reach.</span></div>
      <div class="fact"><span class="fact-num">05</span><span>In Europe, Canada, &amp; Australia healthy breasts are routinely screened with thermography and mammograms are used as a second line of diagnosis.</span></div>
      <div class="fact"><span class="fact-num">06</span><span>For earliest detection and prevention, it is recommended that women receive baseline breast thermography at age 20, every three years between ages 20-30, and annually from age 30.</span></div>
      <div class="fact"><span class="fact-num">07</span><span>Starting breast thermography at any age gives you the safest and earliest detection possible.</span></div>
    </div>
    <div class="q">What are the side effects of Breast Thermography?</div>
    <p>There are no known short or long-term side effects of breast thermography. It is incredibly safe!</p>
    <div class="q">How should I prepare for my Breast Thermography appointment?</div>
    <p>Prior to the test, please adhere to the following:</p>
    <ul class="ticks">
      <li>No natural or artificial tanning 5 days prior to your test date</li>
      <li>No breast manipulation prior to the test, including breast self-exams, compression of the breasts, breast stimulation, breast ultrasound, or mammogram for 24h prior to the test</li>
      <li>No fevers for at least 36h prior to the test</li>
      <li>No steam rooms, saunas, heat packs, or cold packs for at least 4 hours prior to the test</li>
      <li>Do not shave your underarms or use skin creams, lotions, deodorants, or powders on your breast before your test</li>
      <li>No coffee, tea, or tobacco two hours before the test</li>
      <li>No restrictive clothing</li>
    </ul>
    <div class="q">How long will my appointment last?</div>
    <p>Your appointment will last 30-60 minutes.</p>
    <div class="q">When will I get my results?</div>
    <p>Our board certified Physician evaluates each thermographic image and creates a report. Your comprehensive interpretive report, including images, will be ready to follow up within a 7-14 Business days.</p>
  </div>

  <div class="panel pricing-panel">
    <svg class="cover-swoosh" style="top:28px;left:0" width="267" height="50" viewBox="0 0 267 50" aria-hidden="true">
      <path d="M0 40 C80 10 170 5 267 18" stroke="#2a87ad" stroke-width="3" fill="none"/>
      <path d="M0 46 C90 18 180 14 267 26" stroke="#e2737f" stroke-width="2" fill="none"/>
    </svg>
    <div class="cost-box">
      <h2>COST</h2>
      <p>Thermography is not yet paid by insurance companies. For this reason, we consider this an alternative service, not requiring a doctor's order and payable at the time of service. Current rates are as follows:</p>
    </div>
    <table class="fee-table">
      <thead><tr><th>PROCEDURE CODE</th><th>DESCRIPTION</th><th>STANDARD FEE</th></tr></thead>
      <tbody>
        <tr><td>THBRA</td><td><b>Thermogram Breast, Annual</b></td><td>$200.00</td></tr>
        <tr><td>THRO1</td><td>Thermogram 1 Region of Interest (Head, Abdomen, Lower extremities, Upper extremities)</td><td>$180.00</td></tr>
        <tr><td>THROB</td><td>Thermogram 1 Region of Interest With Breasts</td><td>$250.00</td></tr>
        <tr><td>THMHS</td><td>Men's Screen (includes head, neck, thyroid, chest, abdomen, upper and lower back)</td><td>$275.00</td></tr>
        <tr><td>THWHS</td><td>Women's Screen (includes head, neck, thyroid, breast, abdomen/pelvis, upper and lower back)</td><td>$325.00</td></tr>
        <tr><td>THPS</td><td>Thermogram Cervical or Lumbar Study, 3 Sets of images</td><td>$350.00</td></tr>
      </tbody>
    </table>
    <div class="quality-banner">WE PROVIDE THE HIGHEST QUALITY IMAGING AND AFFORDABLE PRICING!</div>
    <div class="call-box">
      <h3>CALL TODAY</h3>
      <p>To schedule your thermography with our office 2140 Harmon Park Dr. Lakeview, TX 79002<br>Telephone: <b>(555) 210-4400</b><br>Fax: (555) 210-4401<br>Web: <b>www.brookhavenhc.com</b></p>
      <p class="tag"><b>1in8 get breast cancer</b> you don't have to be one of them. Call today to let us help you minimize your breast cancer risk and optimize your health.</p>
    </div>
    <div class="thermal-row">
      <div class="thermal-dot" role="img" aria-label="Thermal image of a torso"></div>
      <div class="thermal-dot" role="img" aria-label="Thermal image of a shoulder"></div>
      <div class="thermal-dot" role="img" aria-label="Thermal image of an upper body"></div>
    </div>
  </div>

  <div class="panel cover-panel">
    <div class="cover-photo" role="img" aria-label="Black and white photo of a woman's chest with a hand resting on the breast, glowing red highlight"></div>
    <svg class="cover-swoosh" style="top:48px" width="267" height="40" viewBox="0 0 267 40" aria-hidden="true">
      <path d="M0 0 H267 V14 C180 4 90 20 0 34 Z" fill="#fff"/>
      <path d="M0 34 C90 20 180 4 267 14" stroke="#2a87ad" stroke-width="3" fill="none"/>
      <path d="M0 38 C90 26 180 10 267 20" stroke="#e2737f" stroke-width="1.5" fill="none"/>
    </svg>
    <div class="brand"><span class="brand-dot"></span><span class="brand-name">Brookhaven<br>Family Medicine</span></div>
    <svg class="cover-swoosh" style="top:330px" width="267" height="215" viewBox="0 0 267 215" aria-hidden="true">
      <path d="M0 10 C90 40 180 40 267 0 V215 H0 Z" fill="#fff"/>
      <path d="M0 135 C90 175 190 150 267 120" stroke="#e2737f" stroke-width="3" fill="none"/>
      <path d="M0 145 C100 180 200 160 267 132" stroke="#2a87ad" stroke-width="2" fill="none"/>
    </svg>
    <div class="cover-title"><span class="big">BREAST</span><span class="sub">THERMOGRAPHY</span></div>
    <div class="tagline">
      <div><b>SAFE</b><br><span>SCREENING.</span></div>
      <div><span>EARLY</span><br><b>DETECTION.</b></div>
    </div>
  </div>
</section>

<section class="sheet sheet--inside">

  <div class="panel intro-panel" role="img" aria-label="Soft grey photo of a woman in the background">
    <div class="intro-card">
      <h2>NOW YOU DON'T HAVE TO WAIT TILL YOUR NEXT MAMMOGRAM TO GET A WINDOW INTO YOUR BREAST HEALTH!</h2>
      <p class="lead">Whether you are a busy mom of three, a retired grandmother, or a working woman, your health is your most valuable asset, and you try your best to be on top of taking care of your health.<br><b>So, what about your breast health?<br>Have you had your breast-health checked recently?</b></p>
      <h3><b>PERHAPS</b> YOU:</h3>
      <ul class="ticks">
        <li>Have a family history of breast cancer but are too young for a mammogram</li>
        <li>Are worried about toxic radiation exposure from mammograms</li>
        <li>You have had surgery, implants, or biopsies that might make mammograms difficult to interpret</li>
        <li>Have had an inconclusive mammogram</li>
        <li>Are just plain worried about your breast health</li>
      </ul>
      <p class="callout">No matter which situation you are in, Brookhaven Family Medicine has the perfect solution for you!</p>
      <h3><b>WHY</b> BREAST HEALTH?</h3>
      <p>As you already know, breast health is incredibly important, and breast problems can develop silently for decades before anything can be picked up on a mammogram! Every 2 minutes a woman is diagnosed with Breast Cancer. Every 13 minutes a woman in the US loses her life to breast cancer. More than 250,000 women under 40 in the US live with a breast cancer diagnosis</p>
      <div class="stat-block">
        <div class="stat-badge">
          <div class="stat-figure" role="img" aria-label="Row of eight figures, one highlighted in pink"></div>
          <div class="big">1 IN 8 WOMEN</div>
          <div class="small">WILL DEVELOP BREAST CANCER</div>
        </div>
        <p>About one in eight women in the U.S. will develop invasive breast cancer during her lifetime. Breast cancer is the most common cancer in American women, behind skin cancer, and</p>
      </div>
      <p>second-leading cause of cancer death in women, exceeded only by lung cancer. An estimated 232,670 new cases of invasive breast cancer will be diagnosed in U.S. women this year. Two of three breast cancers are found in women 55 or older and approximately 1/3 of all breast cancers occur in women under 45. Here at Brookhaven Family Medicine, we don't just deal with problems after they have formed. We pride ourselves on comprehensive, preventive health-care to keep you happy and healthy, and this is why we have developed a comprehensive Breast Health Screening Program using state-of-the-art Breast Thermography.</p>
    </div>
  </div>

  <div class="panel info-panel">
    <div class="band"><b>WHAT IS</b> BREAST THERMOGRAPHY?</div>
    <p>Breast Thermography is an exciting addition to breast imaging technology that was approved by the FDA in 1982. It is an additional tool that doctors use to help determine breast cancer risk and can also indicate the risk of other breast conditions. When Breast Thermography is used in combination with other tests, it gives your doctor an improved overall picture of breast health. Breast Thermography uses infra-red imaging technology to scan the breast and produces an incredibly detailed heat map, which can help detect the new blood vessels that grow from tumors, as well as hormonal imbalances, and other breast-health problems. Breast thermography provides an additional piece of the puzzle and is not to be used alone. However, when used together with other imaging and lab tests, it will provide your doctor with much more information, giving a more comprehensive picture of your overall breast health.</p>
    <div class="sub-head"><b>BENEFITS OF</b> BREAST THERMOGRAPHY</div>
    <ul class="ticks benefits">
      <li>No harmful radiation</li><li>Safe</li><li>Fast</li>
      <li>Can be used at any age</li><li>Painless</li><li style="visibility:hidden"></li>
      <li style="grid-column:1/4">No limit on number of tests you can have per year</li>
    </ul>
    <div class="sub-head"><b>WHO SHOULD HAVE</b> BREAST THERMOGRAPHY?</div>
    <ul class="ticks who">
      <li>Women with Fibrocystic Breasts or Dense Breasts</li>
      <li class="note">Dense breast tissue contains more glands and ligaments and less fat. Mammograms have trouble seeing through dense tissue; however thermograms can easily evaluate dense breast tissue.</li>
      <li>Women with inconclusive mammograms</li>
      <li class="note">Thermography can reduce the need for biopsies by up to 20%.</li>
      <li>Women with surgical implants</li>
      <li class="note">The risk of an implant rupturing during a mammogram is a small, but valid concern. With thermography there is no compression and no risk!</li>
      <li>Younger women who want to limit radiation exposure to the breast</li>
      <li class="note">A routine mammogram consists of two views of each breast and contains up to 0.2 rad per x-ray. Radiation accumulates in breast tissue, and each 1.0 rad of exposure increases the risk of breast cancer by 1 percent. Because thermography images thermal heat emanating from the body, there is no radiation risk whatsoever.</li>
      <li>Women with a family history of breast cancer</li>
      <li class="note">Annual breast screening is not usually recommended until age 40; however, if you fall into the high risk category, thermograms should be started in the mid 20's in order to obtain a baseline for all future comparisons.</li>
      <li>Women struggling with hormone imbalance</li>
      <li>Women who want a baseline for overall breast health</li>
      <li>Women who have had surgical procedures or biopsies to the breast</li>
      <li>Women who have had a mastectomy</li>
      <li>You have had an abnormal mammogram and have been told you need to wait 6 months before your next mammogram</li>
      <li>Any man or woman concerned about breast health</li>
    </ul>
  </div>

  <div class="panel compare-panel">
    <div class="band"><b>WHAT IS</b> THE DIFFERENCE BETWEEN A MAMMOGRAM AND BREAST THERMOGRAPHY?</div>
    <p>Unlike a mammogram, which is used to diagnose breast cancer by using X-Rays that find denser tissues, a Breast Thermography Machine uses Infra-Red Imaging to find "hotter" areas of the breast that are more active. A Mammogram is like taking a still photograph that tells you how a breast looks. Breast Thermography is like actively looking through a set of infra-red heat goggles that can tell you how the breast is working. Both tests give us different information and are both important when it comes to assessing your breast health.<br><b>Thermography = Risk | Mammogram = Detection | Biopsy = Diagnosis.</b></p>
    <div class="band"><b>FREQUENTLY ASKED QUESTIONS:</b></div>
    <div class="faq-q">Can I use Breast Thermography instead of a mammogram to diagnose breast cancer?</div>
    <p>No. When it comes to a breast cancer diagnosis, a breast biopsy is the gold-standard for diagnosing breast cancer. Breast Thermography is used together with other tests including mammograms, ultrasounds, MRI's, blood testing, and genetic testing, in order to add incredible amounts of detail to generate a comprehensive picture of your breast health and your risk of breast cancer.</p>
    <div class="faq-q">Thermography? Mammograms? Or both?</div>
    <p>By the time a tumor reaches the size of a pin head (approximately two years into its growth) it can no longer be sustained by the normal blood supply and so it develops its own. The development of that blood supply is called angiogenesis. Thermography is the only technology in place that can detect angiogenesis.</p>
    <svg class="size-chart" width="238" height="34" viewBox="0 0 238 34" aria-hidden="true">
      <circle cx="32" cy="20" r="2" fill="#e2737f"/>
      <circle cx="50" cy="20" r="3" fill="#e2737f"/>
      <circle cx="70" cy="20" r="4" fill="#2a87ad"/>
      <circle cx="92" cy="20" r="5.5" fill="#2a87ad"/>
      <circle cx="118" cy="19" r="8" fill="#b7cf3a"/>
      <circle cx="148" cy="18" r="10" fill="#b7cf3a"/>
      <circle cx="186" cy="16" r="14" fill="#1aa89a"/>
    </svg>
    <div class="chart-labels"><span>Infrared Thermography<br>2mm</span><span>Screening MRI<br>4-8mm</span><span>X-Ray Mammogram<br>12-16mm</span><span>Breast Examination<br>20mm</span></div>
    <p style="margin-top:5px">Mammogram is not early detection. A cancerous tumor has been growing eight to ten years before it is big enough and dense enough to be detected by mammography. That is why the treatment at that stage is so drastic – removal of breast, underlying muscle, lymph nodes, chemotherapy, radiation therapy and hormonal therapy.</p>
    <div class="risk-labels"><span>LOW RISK</span><span>HIGH RISK</span></div>
    <svg width="238" height="10" viewBox="0 0 238 10" aria-hidden="true">
      <rect x="0" y="0" width="238" height="10" rx="5" fill="#9a9a9c"/>
      <circle cx="7" cy="5" r="3" fill="#2a1a3a"/><circle cx="17" cy="5" r="3" fill="#3c1f55"/><circle cx="27" cy="5" r="3" fill="#55205e"/><circle cx="37" cy="5" r="3" fill="#7a1f4e"/><circle cx="47" cy="5" r="3" fill="#1b2d78"/><circle cx="57" cy="5" r="3" fill="#1d4aa0"/><circle cx="67" cy="5" r="3" fill="#2a6fc4"/><circle cx="77" cy="5" r="3" fill="#2a93d4"/><circle cx="87" cy="5" r="3" fill="#25a7b8"/><circle cx="97" cy="5" r="3" fill="#2aa878"/><circle cx="107" cy="5" r="3" fill="#3bb04a"/><circle cx="117" cy="5" r="3" fill="#7cbf3a"/><circle cx="127" cy="5" r="3" fill="#b5cc30"/><circle cx="137" cy="5" r="3" fill="#e6d62e"/><circle cx="147" cy="5" r="3" fill="#f2b72a"/><circle cx="157" cy="5" r="3" fill="#f39428"/><circle cx="167" cy="5" r="3" fill="#ee6d26"/><circle cx="177" cy="5" r="3" fill="#e44626"/><circle cx="187" cy="5" r="3" fill="#d62a2a"/><circle cx="197" cy="5" r="3" fill="#e65a6a"/><circle cx="207" cy="5" r="3" fill="#f08fa0"/><circle cx="217" cy="5" r="3" fill="#f6c2cc"/><circle cx="227" cy="5" r="3" fill="#f6f6f6"/>
    </svg>
    <div class="th-row">
      <div class="th-item"><div class="th-img" role="img" aria-label="Thermogram TH1, normal pattern"></div><div class="th-name">TH 1</div><div class="th-note">is a normal thermogram.</div></div>
      <div class="th-item"><div class="th-img" role="img" aria-label="Thermogram TH2"></div><div class="th-name">TH 2</div><div class="th-note">features are symmetrical, non-complex and moderately vascular. Mostly benign breast changes.</div></div>
      <div class="th-item"><div class="th-img" role="img" aria-label="Thermogram TH3"></div><div class="th-name">TH 3</div><div class="th-note">is associated with atypical breast process. Cysts and adenomas are often represented here.</div></div>
      <div class="th-item"><div class="th-img" role="img" aria-label="Thermogram TH4"></div><div class="th-name">TH 4</div><div class="th-note">is a "positive" thermogram with a significant risk of malignant disease. Further testing advised.</div></div>
      <div class="th-item"><div class="th-img" role="img" aria-label="Thermogram TH5"></div><div class="th-name">TH 5</div><div class="th-note">designates a very high probability of confirming malignant disease. Further diagnostic testing is recommended.</div></div>
    </div>
  </div>
</section>

</body>
</html>
```